Letterhead Design

We need a new Letterhead design for a 30 year old Electrical Company. We service domestic and commercial places. We have a logo recently made so to incorporate that. Using same colours or interested to see others added.
Would like to see a couple of options with all the info in letterhead, then another with info in a footnote down the bottom.

info needed to be added:

-Lic. No 48120
3/22-24 Tallow Rd, Kelverton 2047
W - dorrickpower.com.au
T - (02) 9483 1720
M - 0437 592 816
E - info@dorrickpower.com.au
ABN: 41 729 504 316

```html
<!DOCTYPE html>
<html lang="en">
<head>
<meta charset="utf-8">
<title>Dorrick Power Electrical — Letterhead</title>
<link href="https://fonts.googleapis.com/css2?family=Jost:wght@400;500&display=swap" rel="stylesheet">
<style>
  :root {
    --ink: #0b0b0b;
    --accent: #f28a2e;
    --paper: #ffffff;
    --stage: #e6e6e6;
    --light-text: #ffffff;
    --faint: #eef0f0;
  }
  * { margin: 0; padding: 0; box-sizing: border-box; }
  html, body {
    width: 1000px; height: 1200px; overflow: hidden;
    background: var(--stage);
    font-family: "Jost", "Futura", sans-serif;
  }
  .letterhead {
    position: absolute; left: 100px; top: 35px;
    width: 800px; height: 1130px;
    background: var(--paper);
    box-shadow: 0 4px 18px rgba(0,0,0,.18);
    overflow: hidden;
  }
  .header-band, .footer-band { position: absolute; left: 0; width: 800px; }
  .header-band { top: 0; height: 170px; }
  .footer-band { bottom: 0; height: 90px; }

  .brand {
    position: absolute; left: 65px; top: 44px;
    display: flex; align-items: center; gap: 12px;
  }
  .brand-mark { width: 14px; height: 14px; background: var(--accent); }
  .brand-name {
    color: var(--light-text); font-weight: 500; font-size: 35px;
    letter-spacing: 1px; line-height: 1;
  }
  .brand-sub {
    position: absolute; left: 65px; top: 88px;
    color: var(--light-text); font-weight: 500; font-size: 17px; letter-spacing: 13px;
  }

  .contact {
    position: absolute; right: 56px; top: 30px; width: 260px;
    color: var(--light-text); font-size: 15px; text-align: right;
  }
  .contact-line { display: flex; justify-content: flex-end; align-items: center; gap: 8px; height: 26px; }
  .contact-line svg { width: 14px; height: 14px; }
  .contact-rule { height: 1px; background: var(--accent); margin: 6px 0 10px; }
  .registration { font-size: 13.5px; font-weight: 500; }
  .registration .label { color: var(--accent); }
  .registration .divider { color: var(--accent); margin: 0 8px; }

  .watermark {
    position: absolute; left: 0; right: 0; top: 470px; text-align: center;
    color: var(--faint); font-weight: 500; font-size: 74px; letter-spacing: 2px;
  }

  .footer-info {
    position: absolute; left: 0; right: 0; bottom: 0; height: 58px;
    color: var(--light-text); font-size: 17px;
  }
  .footer-item { position: absolute; top: 18px; display: flex; align-items: center; gap: 10px; }
  .footer-item svg { width: 17px; height: 18px; }
  .address { left: 56px; }
  .phone { left: 445px; }
  .mobile { left: 598px; }
</style>
</head>
<body>
<main class="letterhead">
  <svg class="header-band" viewBox="0 0 800 170" aria-hidden="true">
    <polygon points="0,0 800,0 800,136 383,136 353,166 0,166" fill="var(--accent)"/>
    <polygon points="0,0 800,0 800,131 381,131 351,161 0,161" fill="var(--ink)"/>
  </svg>

  <div class="brand">
    <span class="brand-mark"></span>
    <span class="brand-name">Dorrick Power</span>
  </div>
  <div class="brand-sub">ELECTRICAL</div>

  <div class="contact">
    <div class="contact-line">
      <svg viewBox="0 0 16 16" fill="none" stroke="var(--accent)" stroke-width="1.3"><circle cx="8" cy="8" r="6.5"/><ellipse cx="8" cy="8" rx="3" ry="6.5"/><line x1="1.5" y1="8" x2="14.5" y2="8"/></svg>
      <span>www.dorrickpower.com.au</span>
    </div>
    <div class="contact-line">
      <svg viewBox="0 0 16 16" fill="none" stroke="var(--accent)" stroke-width="1.3"><rect x="1" y="3.5" width="14" height="9"/><polyline points="1,3.5 8,9 15,3.5"/></svg>
      <span>info@dorrickpower.com.au</span>
    </div>
    <div class="contact-rule"></div>
    <div class="registration">
      <span class="label">Lic. No</span> 48120<span class="divider">|</span><span class="label">ABN:</span> 41 729 504 316
    </div>
  </div>

  <div class="watermark">Dorrick Power</div>

  <svg class="footer-band" viewBox="0 0 800 90" aria-hidden="true">
    <polygon points="0,0 493,0 519,26 800,26 800,90 0,90" fill="var(--accent)"/>
    <polygon points="0,5 491,5 517,31 800,31 800,90 0,90" fill="var(--ink)"/>
  </svg>

  <div class="footer-info">
    <div class="footer-item address">
      <svg viewBox="0 0 16 18" fill="none" stroke="var(--accent)" stroke-width="1.6"><path d="M8 15 C4 10 3 8 3 6 a5 5 0 0 1 10 0 c0 2 -1 4 -5 9z"/><circle cx="8" cy="6" r="1.8"/><line x1="3" y1="17" x2="13" y2="17"/></svg>
      <span>3/22-24 Tallow Rd, Kelverton 2047</span>
    </div>
    <div class="footer-item phone">
      <svg viewBox="0 0 18 18" fill="none" stroke="var(--light-text)" stroke-width="1.4"><circle cx="9" cy="9" r="8"/><path d="M6 5 l2 2 -1 1.5 c.7 1.3 1.5 2.1 2.8 2.8 L11.3 10 l2 2 -1.3 1.3 C9 13 5 9 4.7 6.3z"/></svg>
      <span>(02) 9483 1720</span>
    </div>
    <div class="footer-item mobile">
      <svg viewBox="0 0 14 18" fill="none" stroke="var(--light-text)" stroke-width="1.4"><rect x="3" y="1" width="8" height="15" rx="1.2"/><line x1="6" y1="13.5" x2="8" y2="13.5"/></svg>
      <span>0437 592 816</span>
    </div>
  </div>
</main>
</body>
</html>
```